Stonebay Towing Business Card

Towing
Accident towing
Mechanical breakdown
Insurance, salvage and recovery
4wd off road towing
Light & Heavy towing
8347 2516
24 hour business 7 days

Logo can be whole size on front

Industry/Entity Type

Towing/ transport

Contact Information for Business Card

The above

```html
<!DOCTYPE html>
<html lang="en">
<head>
<meta charset="utf-8">
<title>Stonebay Towing – Business Card</title>
<link href="https://fonts.googleapis.com/css2?family=Montserrat:wght@500;700&display=swap" rel="stylesheet">
<style>
  :root {
    --backdrop: #242424;
    --card: #22212a;
    --edge-red: #d8222a;
    --text-light: #f4f4f4;
    --emboss: #2f2e36;
    --emboss-front: #34333b;
  }
  * { box-sizing: border-box; margin: 0; padding: 0; }
  html, body {
    width: 1200px; height: 780px; overflow: hidden;
    background: var(--backdrop);
    font-family: "Montserrat", Arial, sans-serif;
  }
  .stage {
    position: relative; width: 1200px; height: 780px;
    display: flex; align-items: center; justify-content: center; gap: 40px;
  }
  .card {
    position: relative;
    width: 540px; height: 310px;
    background: var(--card);
    border-radius: 22px;
    border-bottom: 6px solid var(--edge-red);
    box-shadow: 0 18px 40px rgba(0,0,0,0.45);
    overflow: hidden;
  }
  .card-front .brand-mark {
    position: absolute; left: 0; right: 0; top: 50%;
    transform: translateY(-50%);
    text-align: center;
    font-weight: 700; font-size: 58px; line-height: 1.05;
    color: var(--emboss-front);
  }
  .card-back .brand-name {
    position: absolute; left: 34px; top: 30px;
    font-weight: 700; font-size: 26px; line-height: 1.05;
    color: var(--text-light);
  }
  .card-back .phone {
    position: absolute; right: 34px; top: 34px;
    display: flex; align-items: center; gap: 10px;
    font-weight: 500; font-size: 16px; letter-spacing: 0.5px;
    color: var(--text-light);
  }
  .phone-icon { width: 16px; height: 16px; fill: var(--edge-red); }
  .services {
    position: absolute; left: 40px; bottom: 28px;
    list-style: none;
  }
  .services li {
    position: relative; padding-left: 20px;
    font-weight: 500; font-size: 13px; line-height: 1.62;
    color: var(--text-light);
  }
  .services li::before {
    content: ""; position: absolute; left: 0; top: 50%;
    width: 8px; height: 8px; margin-top: -4px;
    border-radius: 50%; background: var(--edge-red);
  }
  .card-back .brand-watermark {
    position: absolute; right: 26px; bottom: 34px;
    text-align: right;
    font-weight: 700; font-size: 38px; line-height: 1.05;
    color: var(--emboss);
  }
</style>
</head>
<body>
  <main class="stage">
    <section class="card card-front" aria-label="Card front">
      <div class="brand-mark">Stonebay<br>Towing</div>
    </section>

    <section class="card card-back" aria-label="Card back">
      <div class="brand-name">Stonebay<br>Towing</div>
      <div class="phone">
        <span>8347 2516</span>
        <svg class="phone-icon" viewBox="0 0 24 24" aria-hidden="true">
          <path d="M6.6 10.8a15.1 15.1 0 0 0 6.6 6.6l2.2-2.2a1 1 0 0 1 1-.25 11.4 11.4 0 0 0 3.6.57 1 1 0 0 1 1 1V20a1 1 0 0 1-1 1A17 17 0 0 1 3 4a1 1 0 0 1 1-1h3.5a1 1 0 0 1 1 1c0 1.25.2 2.45.57 3.57a1 1 0 0 1-.25 1z"/>
        </svg>
      </div>
      <ul class="services">
        <li>Towing</li>
        <li>Accident towing</li>
        <li>Mechanical breakdown</li>
        <li>Insurance, salvage and recovery</li>
        <li>4wd off road towing</li>
        <li>Light &amp; Heavy towing</li>
        <li>24/7 business</li>
      </ul>
      <div class="brand-watermark">Stonebay<br>Towing</div>
    </section>
  </main>
</body>
</html>
```